Capability Statement Brochure - Corporate

We need to provide our corporate clients with an elegant, professional and well designed capability statement that not only details what our business can offer, but reflects our professionalism with relevant technical photos. I am thinking two pages A 4 pdf will be suitable if the text can fit without looking crowded but happy to extend to 3 or 4 pages if needed . Colours and details can be taken from our website www.quorintech.com.au Some photos have been attached however if we need more professional stock photos I am happy to use them if needed. This project needs to convince potential clients we are the best in industry and our capability is extensive. Please help us relay this to our customers. Thank you,.

Target Market(s)

Corporate, Government, Education, Defence, Healthcare

Industry/Entity Type

Audio Visual Integration

Colors
0054AA
0677BA
7BADD7
CADEEF
E8F1F8

Requirements
Must have
• Style, look classy, sophisticated and technical
Nice to have
• Quorin Tech colours, Logo, website and email and include the PRISM LED Logo
Should not have
• Messy, too much clutter, not easy to read.

```html
<!DOCTYPE html>
<html lang="en">
<head>
<meta charset="utf-8">
<title>Quorin Tech – Capability Statement 2026</title>
<link href="https://fonts.googleapis.com/css2?family=Montserrat:wght@400;500;600;700&display=swap" rel="stylesheet">
<style>
:root{
  --canvas:#9a9a9a;
  --ink:#3b3d42;
  --heading:#1f4fa0;
  --navy:#2a4aa0;
  --sky:#5b9ee0;
  --rule:#c8d3e2;
  --charcoal:#252527;
  --page-top:#ffffff;
  --page-bottom:#e3ebf5;
}
*{margin:0;padding:0;box-sizing:border-box}
html,body{width:848px;height:1200px;overflow:hidden}
body{background:var(--canvas);font-family:"Montserrat",sans-serif;color:var(--ink);position:relative}
.page{position:absolute;width:393px;height:557px;overflow:hidden;background:linear-gradient(170deg,var(--page-top) 0%,var(--page-bottom) 100%)}
.page-cover{left:20px;top:25px;background:#fff}
.page-sectors{left:432px;top:25px}
.page-overview{left:20px;top:601px}
.page-services{left:432px;top:601px}
.abs{position:absolute}
.photo{position:absolute}
.heading{position:absolute;font-weight:600;color:var(--heading);font-size:13.2px;letter-spacing:.1px;line-height:1;padding-bottom:6px;border-bottom:1px solid var(--rule);white-space:nowrap}
.body{position:absolute;font-size:6.5px;line-height:11.2px}
.body p+p{margin-top:8px}

/* cover */
.brand-mark{left:20px;top:28px;width:26px;height:26px;background:var(--navy)}
.brand-name{left:56px;top:29px;font-size:20px;font-weight:600;color:var(--navy);line-height:1;letter-spacing:.2px}
.brand-tag{left:56px;top:58px;font-size:6.6px;font-weight:500;color:#444;letter-spacing:1px}
.cover-photo{left:0;top:88px;width:380px;height:416px;background:linear-gradient(160deg,#7c8490 0%,#2c3038 40%,#3a3430 75%,#6a5a4a 100%)}
.cover-panel{left:121px;top:246px;width:272px;height:215px;background:var(--charcoal)}
.year-box{left:239px;top:246px;width:88px;height:54px;background:linear-gradient(90deg,var(--navy),var(--sky));color:#fff;font-weight:700;font-size:22px;display:flex;align-items:center;justify-content:center}
.cover-bar{left:112px;top:305px;width:85px;height:8px;background:linear-gradient(90deg,var(--navy),var(--sky))}
.cover-title{left:157px;top:331px;color:#fff;font-weight:700;font-size:33.5px;line-height:47px;letter-spacing:.3px}

/* sectors */
.prism-name{left:20px;top:20px;font-weight:700;font-size:13px;color:#1a1a1a;line-height:1;letter-spacing:.3px}
.why-box{left:204px;top:333px;width:170px;height:215px;background:linear-gradient(160deg,var(--navy),var(--sky));color:#fff;padding:12px 16px}
.why-box h3{font-weight:600;font-size:12.5px;line-height:16px;padding-bottom:7px;border-bottom:1px solid rgba(255,255,255,.4);width:122px}
.why-list{list-style:none;margin-top:9px}
.why-list li{position:relative;padding-left:10px;font-size:6.5px;line-height:10px;margin-bottom:8px}
.why-list li::before{content:"";position:absolute;left:0;top:2.5px;width:4.5px;height:4.5px;background:#fff}

/* overview */
.band{left:0;top:0;width:393px;height:31px;background:linear-gradient(90deg,var(--navy),var(--sky));color:#fff;font-size:14px;font-weight:500;display:flex;align-items:center;justify-content:center;letter-spacing:.4px}
.cap-list{position:absolute;left:20px;top:252px;list-style:none}
.cap-list li{position:relative;padding-left:11px;font-size:6.6px;line-height:15.9px}
.cap-list li::before{content:"";position:absolute;left:0;top:5.5px;width:4px;height:4px;background:var(--navy)}
.markets-box{left:210px;top:228px;width:164px;height:208px;background:linear-gradient(160deg,var(--navy),var(--sky));color:#fff;padding:14px 16px}
.markets-box h3{font-weight:600;font-size:13px;padding-bottom:6px;border-bottom:1px solid rgba(255,255,255,.4);width:122px}
.market-list{list-style:none;margin-top:10px}
.market-list li{display:flex;align-items:center;gap:7px;font-size:6.6px;height:20.5px}
.market-list svg{width:10px;height:10px;flex:none}
</style>
</head>
<body>

<!-- Cover -->
<section class="page page-cover">
  <div class="abs brand-mark"></div>
  <div class="abs brand-name">Quorin Tech</div>
  <div class="abs brand-tag">AUDIOVISUAL INTEGRATION SPECIALISTS</div>
  <div class="photo cover-photo" role="img" aria-label="Dark control room interior with wall-mounted screens and a floating staircase"></div>
  <div class="abs cover-panel"></div>
  <div class="abs year-box">2026</div>
  <div class="abs cover-bar"></div>
  <h1 class="abs cover-title">CAPABILITY<br>STATEMENT</h1>
</section>

<!-- Sectors -->
<section class="page page-sectors">
  <div class="abs prism-name">PRISM LED</div>
  <div class="photo" style="left:20px;top:49px;width:170px;height:92px;background:linear-gradient(160deg,#1c2a48 0%,#2a60b8 45%,#4a88d0 60%,#8a8680 100%)" role="img" aria-label="Large LED video wall showing an underwater scene in a lobby"></div>
  <div class="photo" style="left:204px;top:16px;width:170px;height:97px;background:linear-gradient(150deg,#d8dde2 0%,#b9a89a 50%,#6e737c 100%)" role="img" aria-label="Business colleagues shaking hands in a bright office"></div>

  <h2 class="heading" style="left:20px;top:158px">LED Video Wall Expertise</h2>
  <div class="body" style="left:20px;top:182px;width:178px">
    <p>Quorin Tech has extensive experience designing and installing direct-view LED video walls for corporate environments, education facilities, public venues, and large presentation spaces.</p>
    <p>Our proprietary PRISM LED video wall solutions provide exceptional brightness, durability, and reliability for high-impact display environments such as school halls, gymnasiums, corporate auditoriums, and public venues.</p>
    <p>QT provides complete LED video wall solutions including structural design, engineering certification, installation, commissioning, and ongoing support.</p>
  </div>

  <h2 class="heading" style="left:20px;top:351px">Government &amp; Defence</h2>
  <div class="body" style="left:20px;top:375px;width:160px">
    <p>QT supports government departments and defence organisations with reliable and secure audiovisual systems designed for operational environments including command centres, training facilities, situation rooms, and secure conferencing spaces.</p>
  </div>

  <h2 class="heading" style="left:20px;top:457px;padding-right:25px">Education</h2>
  <div class="body" style="left:20px;top:481px;width:170px">
    <p>QT delivers innovative AV solutions for schools, universities, and training institutions including lecture theatres, classrooms, hybrid learning environments, school halls, gymnasiums, and large-scale LED display systems.</p>
  </div>

  <h2 class="heading" style="left:204px;top:128px">Corporate &amp; Enterprise</h2>
  <div class="body" style="left:204px;top:152px;width:172px">
    <p>QT delivers modern collaboration environments that enable organisations to connect teams across offices, remote staff, and global partners.</p>
    <p>Solutions include boardrooms, hybrid meeting rooms, training facilities, corporate digital signage networks, and executive collaboration spaces.</p>
  </div>

  <h2 class="heading" style="left:204px;top:237px;padding-right:16px">Mining &amp; Resources</h2>
  <div class="body" style="left:204px;top:261px;width:172px">
    <p>QT provides robust AV systems designed for industrial and remote environments including operations centres, training rooms, induction facilities, and remote collaboration systems supporting mining and energy sector operations.</p>
  </div>

  <div class="abs why-box">
    <h3>Why Choose Quorin Tech</h3>
    <ul class="why-list">
      <li>National project delivery capability</li>
      <li>LED video wall specialists</li>
      <li>26+ years audiovisual integration experience</li>
      <li>Proven track record across multiple industries</li>
      <li>In-house design and engineering capability</li>
      <li>Long-term service and support partnerships</li>
    </ul>
  </div>
</section>

<!-- Overview -->
<section class="page page-overview">
  <div class="abs band">QUORIN TECH</div>

  <h2 class="heading" style="left:20px;top:51px;padding-right:18px">Company Overview</h2>
  <div class="body" style="left:20px;top:75px;width:360px">
    <p>Quorin Tech (QT) is a leading Australian audiovisual integration specialist delivering advanced AV, unified communications, collaboration environments, and large-scale digital display systems across Australia.</p>
    <p>With more than 26 years of industry experience, QT provides end-to-end services including system design, engineering, installation, commissioning, and long-term technical support. Our solutions enable organisations to communicate, collaborate, and share information effectively across boardrooms, control centres, training environments, operational facilities, and large public spaces.</p>
    <p>QT works across a broad range of sectors including healthcare, corporate enterprise, government, defence, mining and resources, and education. Our team combines deep technical expertise with a strong understanding of operational environments where reliability, security, and ease of use are essential.</p>
  </div>

  <h2 class="heading" style="left:20px;top:227px;padding-right:26px">Core Capabilities</h2>
  <ul class="cap-list">
    <li>AV System Design and Engineering</li>
    <li>Unified Communications &amp; Collaboration Systems</li>
    <li>LED Video Walls and Large Format Displays</li>
    <li>Control Rooms and Operations Centres</li>
    <li>Boardrooms and Executive Meeting Spaces</li>
    <li>Education and Training Environments</li>
    <li>Digital Signage and Information Display Networks</li>
    <li>AV over IP and Networked Media Systems</li>
    <li>System Programming, Automation and Control</li>
    <li>Ongoing Service, Maintenance &amp; Technical Support</li>
  </ul>

  <div class="abs markets-box">
    <h3>Markets Served</h3>
    <ul class="market-list">
      <li><svg viewBox="0 0 10 10"><circle cx="5" cy="5" r="4.5" fill="#fff"/><path d="M5 2.8v4.4M2.8 5h4.4" stroke="#2a4aa0" stroke-width="1.3"/></svg>Healthcare</li>
      <li><svg viewBox="0 0 10 10"><rect x="2" y="1" width="6" height="8.5" fill="none" stroke="#fff"/><path d="M3.5 3h1M5.5 3h1M3.5 5h1M5.5 5h1M3.5 7h1M5.5 7h1" stroke="#fff"/></svg>Corporate &amp; Enterprise</li>
      <li><svg viewBox="0 0 10 10"><path d="M1 3.5L5 1l4 2.5z" fill="#fff"/><path d="M2.2 4.5v3.5M4 4.5v3.5M6 4.5v3.5M7.8 4.5v3.5M1 9h8" stroke="#fff"/></svg>Government</li>
      <li><svg viewBox="0 0 10 10"><path d="M5 .8l3.6 1.4v2.8c0 2.2-1.6 3.6-3.6 4.2C3 8.6 1.4 7.2 1.4 5V2.2z" fill="none" stroke="#fff"/><path d="M3.3 5l1.2 1.2 2.2-2.3" fill="none" stroke="#fff"/></svg>Defence</li>
      <li><svg viewBox="0 0 10 10"><circle cx="5" cy="5" r="2.2" fill="none" stroke="#fff" stroke-width="1.2"/><path d="M5 .5v2M5 7.5v2M.5 5h2M7.5 5h2M1.8 1.8l1.4 1.4M6.8 6.8l1.4 1.4M1.8 8.2l1.4-1.4M6.8 3.2l1.4-1.4" stroke="#fff"/></svg>Mining &amp; Resources</li>
      <li><svg viewBox="0 0 10 10"><path d="M.5 4L5 2l4.5 2L5 6z" fill="#fff"/><path d="M2.5 5v2c1.5 1 3.5 1 5 0V5" fill="#fff"/></svg>Education</li>
      <li><svg viewBox="0 0 10 10"><path d="M1 2.5h8M1.5 4h7M2 4v5M4 4v5M6 4v5M8 4v5M1 9h8" stroke="#fff"/><path d="M2 2.5L5 1l3 1.5" fill="#fff"/></svg>Public Venues and Event Spaces</li>
    </ul>
  </div>

  <h2 class="heading" style="left:20px;top:440px">Healthcare Experience</h2>
  <div class="body" style="left:20px;top:463px;width:360px">
    <p>QT has extensive experience delivering audiovisual solutions within major healthcare environments including clinical communication systems, specialist consultation rooms, training facilities, and hospital-wide digital signage networks.</p>
    <p>For over 20 years QT has supported Eastbrook General Hospital with the design, implementation, and support of audiovisual infrastructure across departments including ICU, Emergency, Cardiology, Radiology, and Allied Health.</p>
  </div>
</section>

<!-- Services -->
<section class="page page-services">
  <div class="photo" style="left:20px;top:0;width:355px;height:90px;background:linear-gradient(160deg,#c8d0d8 0%,#3c424a 45%,#8a939c 75%,#e4e8ec 100%)" role="img" aria-label="Modern boardroom with a dark conference table, touch panel and laptop"></div>

  <h2 class="heading" style="left:20px;top:108px">Governance, Safety &amp; Compliance</h2>
  <div class="body" style="left:20px;top:132px;width:360px">
    <p>QT operates under strict safety and governance frameworks including OH&amp;S compliant work practices, industry-certified technicians, and full public liability and professional indemnity coverage.</p>
    <p>Safety, compliance, and quality assurance are embedded throughout all project delivery activities.</p>
  </div>

  <h2 class="heading" style="left:20px;top:194px">Implementation &amp; Commissioning</h2>
  <div class="body" style="left:20px;top:218px;width:360px">
    <p>QT delivers complete turnkey project implementation including equipment procurement, professional installation, system configuration, testing, commissioning, and user training.</p>
    <p>Our accredited technicians ensure systems are delivered safely, efficiently, and with minimal disruption to operational environments.</p>
  </div>

  <div class="photo" style="left:20px;top:296px;width:168px;height:116px;background:linear-gradient(150deg,#e4e8ec 0%,#c9a27a 45%,#5d6670 80%,#d8dde2 100%)" role="img" aria-label="Support staff wearing headsets working at computer desks"></div>

  <h2 class="heading" style="left:204px;top:298px">Design &amp; Engineering</h2>
  <div class="body" style="left:204px;top:324px;width:172px">
    <p>QT provides comprehensive in-house design and engineering services including system architecture, documentation, schematics, networked AV design, and integration with existing IT infrastructure.</p>
    <p>Our team works closely with architects, consultants, builders, and project managers to ensure seamless integration of audiovisual technology within new builds and refurbishment projects.</p>
  </div>

  <h2 class="heading" style="left:20px;top:425px;padding-right:15px">Service &amp; Support</h2>
  <div class="body" style="left:20px;top:451px;width:178px">
    <p>QT provides comprehensive ongoing support services including preventative maintenance, priority service response, remote diagnostics, system upgrades, and technology lifecycle planning.</p>
    <p>Our long-term support partnerships ensure systems remain reliable, secure, and aligned with evolving organisational needs.</p>
  </div>

  <div class="photo" style="left:204px;top:446px;width:168px;height:95px;background:linear-gradient(150deg,#cfd6de 0%,#4a5a78 45%,#9aa4b0 100%)" role="img" aria-label="Technicians reviewing equipment together on a workbench"></div>
</section>

</body>
</html>
```